Nine Rung Ledger Remedy Seminar

I would like a flyer to hand out to participants at the speeches that we give. We are a CPA firm that specializes in entrepreneurs and realtors. We would like a flyer that looks crisp and clean, that integrates our logo and our company colors (shades of blue & gold). We would like the wording to be as laid out in the attached documents, but design is up to you. We would like a picture to go along with each point and are open to ideas. The flyer should be one page, preferably just the front.

Colors
3176b5
fee18a

Requirements
Must have
• Our logo and the wording supplied.
• A picture to go along with each topic.
Nice to have
• Images that pop, clean look, professional.
Should not have
• Look messy.

```html
<!DOCTYPE html>
<html lang="en">
<head>
<meta charset="utf-8">
<title>Nine Rung Ledger Remedy Seminar – Agenda Flyer</title>
<link href="https://fonts.googleapis.com/css2?family=Oswald:wght@500;600&family=Montserrat:ital,wght@0,500;0,600;0,700;1,700&family=Libre+Baskerville:ital@1&display=swap" rel="stylesheet">
<style>
  :root{
    --brand-blue:#3176b5;
    --deep-blue:#2a5fa3;
    --gold:#fee18a;
    --tab-dark:#3a3220;
    --ink:#2b2b2b;
    --sky:#d7ecf9;
    --page-bg:#e9ecef;
    --paper:#ffffff;
    --hex-light:#f4f4f4;
    --hex-mid:#e2e2e2;
  }
  *{box-sizing:border-box;margin:0;padding:0}
  html,body{width:1200px;height:1200px;overflow:hidden;background:var(--page-bg)}
  .flyer{position:absolute;left:150px;top:20px;width:900px;height:1160px;background:var(--paper);
    box-shadow:0 6px 20px rgba(0,0,0,.18);overflow:hidden;font-family:"Montserrat",sans-serif}
  .texture{position:absolute;left:0;top:178px;width:900px;height:850px;
    background:linear-gradient(160deg,var(--hex-light),var(--hex-mid) 50%,var(--hex-light))}
  .header{position:absolute;left:0;top:0;width:900px;height:178px}
  .header svg{position:absolute;left:0;top:0}
  .mascot{position:absolute;left:26px;top:14px;width:58px;height:150px;border-radius:29px;
    background:linear-gradient(180deg,#f3c84a 0 10%,#eaf0f7 10% 55%,#1f2f4a 55%)}
  .title{position:absolute;left:108px;top:34px;color:#fff;font-family:"Oswald",sans-serif;
    font-weight:500;font-size:33px;line-height:54px;letter-spacing:.5px;white-space:nowrap}
  .brand{position:absolute;left:625px;top:36px;width:265px;text-align:center}
  .brand-name{font-family:"Oswald",sans-serif;font-weight:600;font-size:40px;color:var(--deep-blue);line-height:1.1;letter-spacing:1px}
  .brand-tag{font-family:"Libre Baskerville",serif;font-style:italic;font-size:12px;color:var(--ink);margin-top:12px}
  .step{position:absolute;left:76px;width:760px;height:100px}
  .step .band{position:absolute;left:40px;top:15px;width:640px;height:70px;padding:0 62px 0 82px;
    display:flex;align-items:center;font-size:12.6px;font-weight:500;line-height:15.5px}
  .step.blue .band{background:var(--brand-blue);color:#fff}
  .step.gold .band{background:var(--gold);color:var(--ink)}
  .step .tab{position:absolute;left:0;top:15px}
  .step .num{position:absolute;left:6px;top:15px;width:72px;height:72px;line-height:72px;
    color:#fff;font-weight:700;font-size:36px}
  .step .icon{position:absolute;left:640px;top:2px;width:98px;height:98px;border-radius:50%;
    border:6px solid var(--deep-blue);box-shadow:0 0 0 3px #fff inset}
  .quote-strip{position:absolute;left:0;top:1020px;width:900px;height:14px;background:var(--sky)}
  .quote{position:absolute;left:0;top:1034px;width:480px;height:74px;background:var(--sky)}
  .quote p{position:absolute;left:30px;top:8px;width:340px;text-align:center;font-weight:700;
    font-style:italic;font-size:15px;color:var(--ink);line-height:20px}
  .quote .mark{position:absolute;left:28px;top:-14px;font-family:"Libre Baskerville",serif;font-size:44px;color:var(--tab-dark)}
  .web{position:absolute;left:0;top:1104px}
  .web span{position:absolute;left:22px;top:8px;font-family:"Oswald",sans-serif;font-weight:500;font-size:31px;color:#fff;white-space:nowrap}
  .company{position:absolute;left:480px;top:1000px;width:420px;text-align:center;color:var(--deep-blue);
    font-weight:700;font-size:16.5px;line-height:20px}
  .contact{position:absolute;left:500px;top:1054px;font-size:12px;font-weight:600;color:var(--deep-blue)}
  .contact li{list-style:none;height:26px;display:flex;align-items:center;gap:10px}
  .contact svg{flex:none}
  .contact .pair{display:flex;gap:26px}
  .contact .pair span{display:flex;align-items:center;gap:10px}
</style>
</head>
<body>
<main class="flyer">
  <div class="texture" role="img" aria-label="Soft grey hexagonal cube background pattern"></div>

  <header class="header">
    <svg width="900" height="178" viewBox="0 0 900 178" aria-hidden="true">
      <polygon points="0,0 535,0 610,178 0,178" fill="var(--deep-blue)"/>
      <rect x="0" y="170" width="900" height="8" fill="#dfe6ef"/>
    </svg>
    <div class="mascot" role="img" aria-label="Cartoon accountant with a light bulb idea above his head"></div>
    <h1 class="title">NINE RUNG LEDGER REMEDY<br>SEMINAR AGENDA</h1>
    <div class="brand">
      <div class="brand-name">TALLYFIELD PARTNERS</div>
      <div class="brand-tag">A Professional Accounting Corporation</div>
    </div>
  </header>

  <section class="steps">
    <div class="step blue" style="top:190px">
      <div class="band">We will first show you how to eliminate much of your self-employment tax on your return by converting your business into an S Corporation. A business owner making over $120,000 per year can save about $12,000 per year by doing this.</div>
      <svg class="tab" width="90" height="72" aria-hidden="true"><path d="M10 0H62L90 36L62 72H10Q0 72 0 62V10Q0 0 10 0Z" fill="var(--tab-dark)"/></svg>
      <div class="num">01</div>
      <div class="icon" role="img" aria-label="Hand pulling a TAX sign, illustration" style="background:radial-gradient(circle,#cfe3da,#9fc4b8)"></div>
    </div>
    <div class="step gold" style="top:303px">
      <div class="band">We will show you how to get tax free income from your corporation by renting you home to the corporation for the board meetings.Many of our clients are getting up to $21,000 in tax free income which could put $8,400 cash into your pocket.</div>
      <svg class="tab" width="90" height="72" aria-hidden="true"><path d="M10 0H62L90 36L62 72H10Q0 72 0 62V10Q0 0 10 0Z" fill="var(--tab-dark)"/></svg>
      <div class="num">02</div>
      <div class="icon" role="img" aria-label="House with keys, illustration" style="background:radial-gradient(circle,#f1f4f8,#b9c7d8)"></div>
    </div>
    <div class="step blue" style="top:416px">
      <div class="band">We will show you the easiest way to track your expenses so that the only thing you will have to do to have rock solid books is to take a picture of the receipt and throw it away.It doesn't get any better than that.</div>
      <svg class="tab" width="90" height="72" aria-hidden="true"><path d="M10 0H62L90 36L62 72H10Q0 72 0 62V10Q0 0 10 0Z" fill="var(--tab-dark)"/></svg>
      <div class="num">03</div>
      <div class="icon" role="img" aria-label="Hand tapping a smartphone, illustration" style="background:radial-gradient(circle,#ffffff,#d7e3ee)"></div>
    </div>
    <div class="step gold" style="top:529px">
      <div class="band">Next, we show you the importance of tax planning and why it is critical to meet with your CPA before the end of the year and not just when you do your tax preparation.</div>
      <svg class="tab" width="90" height="72" aria-hidden="true"><path d="M10 0H62L90 36L62 72H10Q0 72 0 62V10Q0 0 10 0Z" fill="var(--tab-dark)"/></svg>
      <div class="num">04</div>
      <div class="icon" role="img" aria-label="Hand holding a calculator over a tax form, illustration" style="background:radial-gradient(circle,#cfeaf8,#7fc0e6)"></div>
    </div>
    <div class="step blue" style="top:642px">
      <div class="band">We will show you how to hire your children and get $7,500 per child tax free.This will save you $3,000 per child in income tax reduction.</div>
      <svg class="tab" width="90" height="72" aria-hidden="true"><path d="M10 0H62L90 36L62 72H10Q0 72 0 62V10Q0 0 10 0Z" fill="var(--tab-dark)"/></svg>
      <div class="num">05</div>
      <div class="icon" role="img" aria-label="Tax documents with calculator and cash, illustration" style="background:radial-gradient(circle,#f7f7f2,#cfd9c4)"></div>
    </div>
    <div class="step gold" style="top:755px">
      <div class="band">We will discuss how to make your child's college education tax deductible. With college cost spiraling out of control this is a biggie.&nbsp; Most of our clients have a savings of about $12,000 per year of college.</div>
      <svg class="tab" width="90" height="72" aria-hidden="true"><path d="M10 0H62L90 36L62 72H10Q0 72 0 62V10Q0 0 10 0Z" fill="var(--tab-dark)"/></svg>
      <div class="num">06</div>
      <div class="icon" role="img" aria-label="Graduate in cap and gown, illustration" style="background:radial-gradient(circle,#f6a64a,#e0731f)"></div>
    </div>
    <div class="step blue" style="top:868px">
      <div class="band">Our grand finale is to show you how to use, not one, but two corporations to get a several hundred thousand dollar tax deferral, get an interest free loan from the government and use that money to grow your business and your wealth.</div>
      <svg class="tab" width="90" height="72" aria-hidden="true"><path d="M10 0H62L90 36L62 72H10Q0 72 0 62V10Q0 0 10 0Z" fill="var(--tab-dark)"/></svg>
      <div class="num">07</div>
      <div class="icon" role="img" aria-label="Busy businessman at a desk with charts, illustration" style="background:radial-gradient(circle,#ffffff,#dde6f0)"></div>
    </div>
  </section>

  <footer>
    <div class="quote-strip"></div>
    <div class="quote">
      <span class="mark">“</span>
      <p>If they drive by with a machine gun<br>you don't have to stand up.</p>
    </div>
    <div class="web">
      <svg width="430" height="56" aria-hidden="true"><polygon points="0,0 430,0 410,56 0,56" fill="var(--deep-blue)"/></svg>
      <span>WWW.TALLYFIELDCPA.COM</span>
    </div>
    <div class="company">Tallyfield Partners,<br>A Professional Accounting Corporation</div>
    <ul class="contact">
      <li><svg width="14" height="16" viewBox="0 0 14 16" aria-hidden="true"><path d="M7 0C3.5 0 1 2.6 1 6c0 4 6 10 6 10s6-6 6-10C13 2.6 10.5 0 7 0z" fill="#d93a3a"/><circle cx="7" cy="6" r="2.2" fill="#fff"/></svg>2870 Orchard Ave, Ste. B, Linden Vale, CA 95012</li>
      <li class="pair">
        <span><svg width="15" height="15" viewBox="0 0 16 16" aria-hidden="true"><circle cx="8" cy="8" r="8" fill="#1a9b8a"/><path d="M5 4l2 2-1 1c.6 1.3 1.7 2.4 3 3l1-1 2 2-1.4 1.4C7.5 12 4 8.5 3.6 5.4z" fill="#fff"/></svg>Phone: 555-014-2231</span>
        <span><svg width="16" height="14" viewBox="0 0 16 14" aria-hidden="true"><rect x="3" y="0" width="10" height="5" fill="#444"/><rect x="0" y="5" width="16" height="6" rx="1" fill="#444"/><rect x="3" y="9" width="10" height="5" fill="#888"/></svg>Fax: 555-014-2290</span>
      </li>
      <li><svg width="16" height="14" viewBox="0 0 16 14" aria-hidden="true"><rect width="16" height="14" rx="2" fill="#e8b92c"/><path d="M1 2l7 5 7-5" stroke="#fff" stroke-width="1.6" fill="none"/></svg>ellis@tallyfieldcpa.com</li>
      <li><svg width="16" height="14" viewBox="0 0 16 14" aria-hidden="true"><rect width="16" height="14" rx="2" fill="#f08a3a"/><path d="M1 2l7 5 7-5" stroke="#fff" stroke-width="1.6" fill="none"/></svg>morgan@tallyfieldcpa.com</li>
    </ul>
  </footer>
</main>
</body>
</html>
```